Safety Training company business card design

We are after a high quality, professional business card. We are open to a single or double sided card.

The winning designer must provide the card in a format where we can easily change the name and details of the different people in our organization.

Harbor Guard's company colour is lime green.

We provide all aspects of safety advisory and training for the Building, Civil Construction, Mining, Oil and Gas, Manufacturing, Rail, Rural and Retail sectors.

Visit our website www.harborguard.com.au for training competencies we offer along with our other services including RPL's, safety audits, professional development and client support.

Target Market(s)

Those in the Building, Civil Construction, Mining, Oil and Gas, Manufacturing, Rail, Rural and Retail industries.

Industry/Entity Type

Training

Contact Information for Business Card

Harbor Guard
Safety and Training
Dennis Palworth
Director
M 0427 518 266
dennis@harborguard.com.au
www.harborguard.com.au
(2 business addresses:)
Corvin High Risk Training Centre
17 Tandem Parade, Corvin Q 4215 P 3912 5486 F 3912 5174
Brenlow Training Centre
86 Fenwick Street, Brenlow Q 4790 P 4873 2615 F 4873 2249

Colors
9bcb3c

Requirements
Must have
• Lime green must be the main colour. must include HG logo attached, and state Harbor Guard (Safety and Training in smaller/different font).

State something along the lines of:

Nice to have
• We offer remote training and we can come to you.

```html
<!DOCTYPE html>
<html lang="en">
<head>
<meta charset="utf-8">
<title>Harbor Guard – Business Card</title>
<link rel="stylesheet" href="https://fonts.googleapis.com/css2?family=Arimo:wght@400;700&display=swap">
<style>
  :root {
    --lime: #8cff00;
    --frame: #5fef3c;
    --paper: #ffffff;
    --card-shadow: rgba(0, 0, 0, 0.16);
    --white-text: #ffffff;
  }
  * { margin: 0; padding: 0; box-sizing: border-box; }
  html, body {
    width: 1200px;
    height: 754px;
    overflow: hidden;
    background: var(--paper);
  }
  .canvas {
    position: relative;
    width: 1200px;
    height: 754px;
    border: 1px solid var(--frame);
    background: var(--paper);
    font-family: "Arimo", Arial, sans-serif;
  }
  .card {
    position: absolute;
    top: 151px;
    height: 315px;
    background: var(--paper);
    box-shadow: 0 0 3px var(--card-shadow);
    overflow: hidden;
  }
  .card--front { left: 82px; width: 500px; }
  .card--back { left: 618px; width: 520px; }

  /* Front */
  .brand {
    position: absolute;
    left: 24px;
    top: 82px;
    display: flex;
    flex-direction: column;
    align-items: flex-start;
  }
  .brand__mark {
    width: 46px;
    height: 46px;
    margin-left: 77px;
    margin-bottom: 22px;
  }
  .brand__name {
    display: inline-block;
    font-size: 20px;
    font-weight: 700;
    color: var(--lime);
    letter-spacing: -0.3px;
    white-space: nowrap;
    transform: scaleX(0.8);
    transform-origin: left center;
  }
  .person {
    position: absolute;
    right: 21px;
    top: 64px;
    text-align: right;
    color: var(--lime);
  }
  .person__name {
    font-size: 22px;
    font-weight: 700;
    line-height: 1;
  }
  .person__role {
    font-size: 16px;
    font-weight: 400;
    line-height: 1.05;
  }
  .contact {
    position: absolute;
    right: 21px;
    top: 186px;
    text-align: right;
    list-style: none;
    color: var(--lime);
    font-size: 14px;
    font-weight: 700;
    line-height: 17.5px;
  }

  /* Back */
  .band {
    position: absolute;
    left: 0;
    top: 0;
    width: 100%;
    height: 169px;
    background: var(--lime);
  }
  .office {
    position: absolute;
    font-style: normal;
    font-size: 18px;
    font-weight: 700;
    line-height: 22.3px;
    white-space: nowrap;
  }
  .office--upper { left: 262px; top: 12px; color: var(--white-text); }
  .office--lower { left: 24px; top: 181px; color: var(--lime); }
</style>
</head>
<body>
<main class="canvas">
  <section class="card card--front" aria-label="Card front">
    <div class="brand">
      <svg class="brand__mark" viewBox="0 0 46 46" aria-hidden="true">
        <circle cx="23" cy="23" r="23" fill="var(--lime)"/>
      </svg>
      <span class="brand__name">Harbor Guard and Training</span>
    </div>
    <div class="person">
      <p class="person__name">Dennis Palworth</p>
      <p class="person__role">Director</p>
    </div>
    <ul class="contact">
      <li>M: 0427518266</li>
      <li>Web: www.harborguard.com.au</li>
      <li>Email: dennis@harborguard.com.au</li>
    </ul>
  </section>

  <section class="card card--back" aria-label="Card back">
    <div class="band"></div>
    <address class="office office--upper">
      Brenlow Training Centre<br>
      86 Fenwick Street<br>
      Brenlow Q 4790<br>
      P: 48732615<br>
      F: 48732249
    </address>
    <address class="office office--lower">
      Corvin High Risk Training Centre<br>
      17 Tandem Parade<br>
      Corvin Q 4215<br>
      P: 39125486<br>
      F: 39125174
    </address>
  </section>
</main>
</body>
</html>
```